Cover für Erstlingswerk
Ich habe von Ralosa ein phantastisches Cover für mein Buch bekommen. Ganz anders als ich es mir bei Auftragsstellung vorgestellt habe. Sehr innovativ und außergewöhnlich. Die Zusammenarbeit war freundlich und locker, spontan und flexibel. Ich bedanke mich ganz herzlich für dieses wundervolle Cover für mein Herzensprojekt!
Zielgruppe
Es handelt sich um einen Roman, der insbesondere Frauen zwischen 30 und 60 Jahren ansprechen wird.
Aufgabenstellung
Das Cover soll schlicht, ohne Schnörkel sein, bevorzugte Farben blau wie die Nordsee und der Himmel, grün und braun wie der Kiefernwald und das Dünengras und weiß wie die Wolken. Ggf. ein Bezug zu Dänemark. Aber ich bin für alle Ideen offen.
Noch ein Nachtrag: dies ist mein erster Auftrag und mein erstes Buch, daher, wenn es Fragen gibt, bitte stellen. Ich habe auch einen Klappentext, wird der zu diesem Zeitpunkt schon eingebunden? Es steckt viel Herzblut und Zeit in meinem ersten Roman. Wenn ich für das Cover mehr Input geben soll, bitte mitteilen!
Noch ein Nachtrag: Der Titel des Buches lautet "Wo der Wind mich fand" und der Name der Autorin Marla Thorvik.

```html
<!DOCTYPE html>
<html lang="de">
<head>
<meta charset="utf-8">
<title>Wo der Wind mich fand – Marla Thorvik</title>
<link rel="stylesheet" href="https://fonts.googleapis.com/css2?family=Overlock:ital,wght@0,400;1,400&family=Dancing+Script:wght@500&display=swap">
<style>
  :root {
    --sand-light: #e8e0d5;
    --sand-mid: #ddd3c7;
    --sand-dark: #cfc6bb;
    --slate-blue: #3e5a68;
    --night-navy: #1d2c3c;
    --storm-blue: #4a6677;
    --sea-teal: #5f9490;
    --dune-green: #3a4f43;
    --shore-brown: #3b3a32;
    --cloud-white: #ffffff;
  }
  * { margin: 0; padding: 0; box-sizing: border-box; }
  html, body {
    width: 768px;
    height: 1200px;
    overflow: hidden;
  }
  .cover {
    position: relative;
    width: 768px;
    height: 1200px;
    overflow: hidden;
  }
  .cover__backdrop {
    position: absolute;
    inset: 0;
    background:
      radial-gradient(ellipse at 30% 20%, var(--sand-light) 0%, transparent 60%),
      linear-gradient(160deg, var(--sand-mid) 0%, var(--sand-light) 45%, var(--sand-dark) 100%);
  }
  .cover__portrait {
    position: absolute;
    left: 90px;
    top: 208px;
    width: 600px;
    height: 992px;
    border-radius: 300px 300px 0 0;
    background: linear-gradient(180deg,
      var(--night-navy) 0%,
      var(--storm-blue) 38%,
      #6c8591 55%,
      var(--sea-teal) 72%,
      var(--dune-green) 90%,
      var(--shore-brown) 100%);
  }
  .cover__author {
    position: absolute;
    top: 78px;
    left: 0;
    width: 100%;
    text-align: center;
    font-family: "Overlock", sans-serif;
    font-size: 56px;
    letter-spacing: 1px;
    color: var(--slate-blue);
  }
  .cover__title {
    position: absolute;
    left: 0;
    top: 0;
    font-family: "Dancing Script", cursive;
    font-weight: 500;
    color: var(--cloud-white);
  }
  .cover__title-line {
    position: absolute;
    white-space: nowrap;
    line-height: 1;
  }
  .cover__title-line--first { left: 190px; top: 370px; font-size: 140px; }
  .cover__title-line--second { left: 170px; top: 560px; font-size: 140px; }
  .cover__title-line--third { left: 170px; top: 800px; font-size: 230px; }
  .cover__genre {
    position: absolute;
    left: 572px;
    top: 852px;
    font-family: "Overlock", sans-serif;
    font-style: italic;
    font-size: 42px;
    color: var(--slate-blue);
  }
</style>
</head>
<body>
  <main class="cover">
    <div class="cover__backdrop" role="img" aria-label="Feine, helle Sandfläche mit Wasserspuren"></div>
    <div class="cover__portrait" role="img" aria-label="Silhouette einer Frau im Profil, gefüllt mit Sturmwolken, Nordsee und Strand"></div>
    <p class="cover__author">Marla Thorvik</p>
    <h1 class="cover__title">
      <span class="cover__title-line cover__title-line--first">Wo der</span>
      <span class="cover__title-line cover__title-line--second">Wind mich</span>
      <span class="cover__title-line cover__title-line--third">fand</span>
    </h1>
    <p class="cover__genre">Roman</p>
  </main>
</body>
</html>
```